Business Card & Letterhead

We are a Raw, Vegan, Organic dessert company in Australia.

We require a new look Business Card and letterhead. Currently we are re-branding and therefore need designs to fit the new look.

Our signature Blue color is definitely still a preference to have as a dominant color in your design.

The feel of the brand is fresh, quirky and healthy. Provide your best design that you believe fits our brand.

Visit our website [login to view URL] and instagram to get a feel for the company branding and feel.

Please provide creative and original designs, do not copy each others designs.

Final files must be submitted as PSD LAYERED FILES
with editable text.

View the very old designs in the below dropbox folder:

```html
<!DOCTYPE html>
<html lang="en">
<head>
<meta charset="utf-8">
<title>purebite desserts – stationery</title>
<link rel="stylesheet" href="https://fonts.googleapis.com/css2?family=Lato:wght@400;700&family=Parisienne&display=swap">
<style>
  :root{
    --sky:#6dd0ea;
    --sky-deep:#4ec3e2;
    --periwinkle:#7a8fd0;
    --tan:#b89c6c;
    --tan-light:#dcc69c;
    --ink:#2e2e30;
    --ink-soft:#55575c;
    --paper:#ffffff;
    --backdrop:#e8e9eb;
  }
  *{box-sizing:border-box;margin:0;padding:0}
  html,body{width:849px;height:1200px;overflow:hidden;background:var(--backdrop)}
  body{font-family:"Lato",Arial,sans-serif;color:var(--ink)}
  .canvas{position:relative;width:849px;height:1200px;overflow:hidden;background:var(--backdrop)}

  /* shared */
  .wordmark{font-family:"Lato",Arial,sans-serif;font-weight:400;color:var(--tan);letter-spacing:-0.5px;line-height:1}
  .tagline{font-family:"Parisienne",cursive;color:var(--sky-deep);line-height:1;white-space:nowrap}
  .stripe-sky{position:absolute;top:0;bottom:0;background:var(--sky)}
  .stripe-peri{position:absolute;top:0;bottom:0;background:var(--periwinkle)}
  .icon-tab{position:absolute;background:var(--sky);border-radius:0 12px 12px 0;display:flex;flex-direction:column;align-items:center;justify-content:center}
  .icon-tab svg{display:block;fill:#fff}
  .contact-list{position:absolute;list-style:none;color:var(--ink-soft)}

  /* business card front */
  .card{position:absolute;width:340px;height:190px;left:254px;box-shadow:0 6px 14px rgba(0,0,0,.18)}
  .card-front{top:60px;background:var(--paper)}
  .card-front .stripe-sky{left:0;width:9px}
  .card-front .stripe-peri{left:12px;width:5px}
  .card-front .holder{position:absolute;left:36px;top:26px}
  .card-front .holder-name{font-weight:700;font-size:11px}
  .card-front .holder-role{font-size:8.5px;color:var(--ink-soft);margin-top:2px}
  .card-front .wordmark{position:absolute;right:14px;top:20px;font-size:34px}
  .card-front .icon-tab{left:9px;top:71px;width:20px;height:66px;gap:4px}
  .card-front .contact-list{left:36px;top:74px;font-size:8px;line-height:11.4px}
  .card-front .tagline{position:absolute;left:48px;top:146px;font-size:21px}

  /* business card back */
  .card-back{top:290px;background:var(--sky);text-align:center}
  .card-back .wordmark{position:absolute;left:0;right:0;top:52px;font-size:40px;color:var(--tan-light)}
  .card-back .sub{position:absolute;left:186px;top:96px;font-family:"Parisienne",cursive;font-size:12px;color:#eaf8fc}
  .card-back .values{position:absolute;left:0;right:0;top:146px;font-size:7.5px;letter-spacing:1px;color:#fff;word-spacing:16px}

  /* letterhead */
  .letterhead{position:absolute;left:191px;top:520px;width:466px;height:660px;background:var(--paper);box-shadow:0 6px 16px rgba(0,0,0,.16);font-size:7.4px;color:var(--ink-soft)}
  .letterhead .stripe-sky{left:12px;width:12px}
  .letterhead .stripe-peri{left:28px;width:5px}
  .letterhead .wordmark{position:absolute;left:52px;top:38px;font-size:28px}
  .letterhead .date{position:absolute;right:40px;top:70px}
  .letterhead .recipient{position:absolute;left:52px;top:92px;line-height:10px;color:var(--ink)}
  .letterhead .recipient b{font-weight:700}
  .letterhead .body{position:absolute;left:52px;top:150px;width:370px;line-height:10.5px}
  .letterhead .body p{margin-bottom:10px}
  .letterhead .signature{position:absolute;left:52px;top:318px;width:60px;height:22px;background:linear-gradient(90deg,#f1f1f3,#e3e4e8);border-radius:3px}
  .letterhead .signer{position:absolute;left:52px;top:346px;color:var(--ink)}
  .letterhead .tagline{position:absolute;right:40px;top:548px;font-size:22px}
  .letterhead .icon-tab{left:24px;top:578px;width:20px;height:62px;gap:3.5px}
  .letterhead .contact-list{left:52px;top:580px;font-size:7.2px;line-height:11px}
</style>
</head>
<body>
<main class="canvas">

  <!-- Business card: front -->
  <section class="card card-front" aria-label="Business card front">
    <span class="stripe-sky"></span>
    <span class="stripe-peri"></span>
    <div class="holder">
      <p class="holder-name">Mila Dorsen</p>
      <p class="holder-role">Manager</p>
    </div>
    <p class="wordmark">purebite</p>
    <div class="icon-tab" aria-hidden="true">
      <svg width="7" height="7" viewBox="0 0 10 10"><path d="M2 0.5l2 2-1 1.3c.6 1.3 1.6 2.3 2.9 2.9l1.3-1 2 2-1.2 1.8C4.5 9.2.8 5.5.3 1.7z"/></svg>
      <svg width="7" height="6" viewBox="0 0 10 8"><path d="M0 0h10v8H0z M0.8 0.8L5 4.2 9.2 0.8" stroke="#6dd0ea" stroke-width="0.8"/></svg>
      <svg width="7" height="7" viewBox="0 0 10 10"><circle cx="5" cy="5" r="4.5" fill="none" stroke="#fff" stroke-width="1"/><path d="M0.5 5h9M5 0.5v9" stroke="#fff" stroke-width="0.8"/></svg>
      <svg width="6" height="6" viewBox="0 0 10 10"><circle cx="5" cy="5" r="5"/></svg>
      <svg width="6" height="6" viewBox="0 0 10 10"><circle cx="5" cy="5" r="5"/></svg>
    </div>
    <ul class="contact-list">
      <li>0400 555 728</li>
      <li>mila@purebitedesserts.com</li>
      <li>www.purebitedesserts.com.au</li>
      <li>www.social.purebitedesserts.com</li>
      <li>purebitedesserts</li>
    </ul>
    <p class="tagline">‘keep it raw, make it fun’</p>
  </section>

  <!-- Business card: back -->
  <section class="card card-back" aria-label="Business card back">
    <p class="wordmark">purebite</p>
    <p class="sub">desserts</p>
    <p class="values">RAW VEGAN ORGANIC</p>
  </section>

  <!-- Letterhead -->
  <section class="letterhead" aria-label="Letterhead">
    <span class="stripe-sky"></span>
    <span class="stripe-peri"></span>
    <p class="wordmark">purebite</p>
    <p class="date">Date: 14-11-2018</p>
    <div class="recipient">
      <p><b>Dear Sir</b></p>
      <p><b>Mila Dorsen</b></p>
      <p>Sub: Application For Mission</p>
      <p><b>Address:</b> 48 Harbour Lane,</p>
      <p>2nd Floor Byron Bay NSW 2481</p>
    </div>
    <div class="body">
      <p>Thank you for your interest in our raw dessert range. We are pleased to share the details of our latest seasonal menu and wholesale options with you today. Our team has prepared a short overview of pricing, minimum orders and delivery days for cafes across the region, along with notes on storage and shelf life.</p>
      <p>Every cake is handmade in small batches using organic nuts, fruit and cold pressed oils. We never use refined sugar, dairy or gluten, and each order is packed fresh to travel well. Our kitchen is certified organic and every recipe is tested by our team before it joins the menu.</p>
      <p>Please let us know which flavours suit your cafe and we will arrange a tasting box for your team next week. We look forward to working with you and sharing a little sweetness with your customers.</p>
    </div>
    <div class="signature" role="img" aria-label="Handwritten signature"></div>
    <p class="signer">Owen R. Hale</p>
    <p class="tagline">‘keep it raw, make it fun’</p>
    <div class="icon-tab" aria-hidden="true">
      <svg width="6" height="6" viewBox="0 0 10 10"><path d="M2 0.5l2 2-1 1.3c.6 1.3 1.6 2.3 2.9 2.9l1.3-1 2 2-1.2 1.8C4.5 9.2.8 5.5.3 1.7z"/></svg>
      <svg width="6" height="5" viewBox="0 0 10 8"><path d="M0 0h10v8H0z M0.8 0.8L5 4.2 9.2 0.8" stroke="#6dd0ea" stroke-width="0.8"/></svg>
      <svg width="6" height="6" viewBox="0 0 10 10"><circle cx="5" cy="5" r="4.5" fill="none" stroke="#fff" stroke-width="1"/><path d="M0.5 5h9M5 0.5v9" stroke="#fff" stroke-width="0.8"/></svg>
      <svg width="5" height="5" viewBox="0 0 10 10"><circle cx="5" cy="5" r="5"/></svg>
      <svg width="5" height="5" viewBox="0 0 10 10"><circle cx="5" cy="5" r="5"/></svg>
    </div>
    <ul class="contact-list">
      <li>0400 555 728</li>
      <li>mila@purebitedesserts.com</li>
      <li>www.purebitedesserts.com.au</li>
      <li>www.social.purebitedesserts.com</li>
      <li>purebitedesserts</li>
    </ul>
  </section>

</main>
</body>
</html>
```